Duel Business card

Want an edgy business card that shows both of our companies on each side of the card, OR both together with a cool design.

*Must be edgy: We have attached our two business logos. We are a bail bond and immigration bond company.

Would like the address on one side only.
Need Phone, cell, website, address, and Name

Company Name 1: Cellgate Release Partners
www.cellgatereleasepartners.example

Company Name 2: Borderline Surety Associates
www.borderlinesuretyassociates.example

These cards will need to be easily changeable so I can modify new employees

Target Market(s)

people in jail, takign imigrants out of jail and from being taken back to there country

Industry/Entity Type

Business

Requirements
Must have
• Include both logos attached

```html
<!DOCTYPE html>
<html lang="en">
<head>
<meta charset="utf-8">
<title>Business Card – Front and Back</title>
<link href="https://fonts.googleapis.com/css2?family=Arimo:wght@400;700&display=swap" rel="stylesheet">
<style>
  :root {
    --page: #ffffff;
    --card: #ffffff;
    --navy: #1c3f66;
    --gold: #f1c232;
    --brand-blue: #1f3f8f;
    --name-blue: #1b5a8c;
    --text: #4a4a4a;
    --divider: #c9c9c9;
    --mark: #d9dfeb;
  }
  * { box-sizing: border-box; margin: 0; padding: 0; }
  html, body {
    width: 1200px; height: 900px; overflow: hidden;
    background: var(--page);
    font-family: "Arimo", Arial, sans-serif;
  }
  .stage { position: relative; width: 1200px; height: 900px; }

  .card {
    position: absolute; left: 293px; width: 616px; height: 353px;
    background: var(--card); overflow: hidden;
    box-shadow: 4px 5px 8px rgba(0,0,0,0.25);
  }
  .card--front { top: 67px; }
  .card--back { top: 478px; }

  .card__waves { position: absolute; left: 0; top: 0; width: 616px; height: 353px; }

  .brand { position: absolute; display: flex; flex-direction: column; align-items: center; text-align: center; }
  .brand__circle { border-radius: 50%; background: var(--mark); border: 3px solid var(--brand-blue); }
  .brand__name {
    margin-top: 8px; color: var(--brand-blue); font-weight: 700;
    font-size: 15px; line-height: 1.2; width: 230px;
  }

  .front__brands { position: absolute; left: 32px; top: 30px; width: 230px; }
  .front__brands .brand { position: static; }
  .front__brands .brand + .brand { margin-top: 16px; }

  .divider { position: absolute; left: 307px; top: 67px; width: 1px; height: 193px; background: var(--divider); }

  .contact { position: absolute; left: 359px; top: 86px; color: var(--text); font-size: 15px; }
  .contact__name { color: var(--name-blue); font-weight: 700; font-size: 21px; }
  .contact__title { margin-top: 4px; font-size: 15px; }
  .contact__address { margin-top: 20px; line-height: 20px; }
  .contact__line { display: flex; align-items: center; gap: 6px; line-height: 21px; }
  .contact__icon { width: 13px; height: 13px; flex: none; }

  .back__brand { top: 56px; width: 280px; }
  .back__brand--left { left: 33px; }
  .back__brand--right { left: 320px; }
  .back__url { margin-top: 12px; color: var(--text); font-size: 13.5px; white-space: nowrap; }
</style>
</head>
<body>
<main class="stage">

  <section class="card card--front">
    <svg class="card__waves" viewBox="0 0 616 353" aria-hidden="true">
      <path fill="var(--gold)" d="M0,283 C150,298 300,330 420,302 C505,282 560,262 616,253 L616,353 L0,353 Z"/>
      <path fill="var(--navy)" d="M0,309 C150,318 300,348 430,330 C520,316 580,299 616,291 L616,353 L0,353 Z"/>
    </svg>

    <div class="front__brands">
      <div class="brand">
        <div class="brand__circle" style="width:72px;height:72px"></div>
        <div class="brand__name">Borderline Surety Associates</div>
      </div>
      <div class="brand">
        <div class="brand__circle" style="width:56px;height:56px"></div>
        <div class="brand__name">Cellgate Release Partners</div>
      </div>
    </div>

    <div class="divider"></div>

    <div class="contact">
      <div class="contact__name">Daniel Whitfield</div>
      <div class="contact__title">Founder &amp; CEO</div>
      <div class="contact__address">4175 Larkspur Avenue<br>Fairbrook, VA 22019</div>
      <div class="contact__line">
        <svg class="contact__icon" viewBox="0 0 14 14" aria-label="Phone">
          <circle cx="7" cy="7" r="7" fill="var(--name-blue)"/>
          <path d="M4.3,3.5 L5.8,3.5 L6.3,5.3 L5.4,6 C5.9,7.1 6.9,8.1 8,8.6 L8.7,7.7 L10.5,8.2 L10.5,9.7 C7,10 4,7 4.3,3.5 Z" fill="#fff"/>
        </svg>
        <span>(555) 214-3870</span>
      </div>
      <div class="contact__line">
        <svg class="contact__icon" viewBox="0 0 14 14" aria-label="Mobile">
          <circle cx="7" cy="7" r="7" fill="var(--name-blue)"/>
          <rect x="4.8" y="3" width="4.4" height="8" rx="0.8" fill="#fff"/>
          <rect x="5.5" y="4" width="3" height="5" fill="var(--name-blue)"/>
        </svg>
        <span>(555) 214-3870</span>
      </div>
    </div>
  </section>

  <section class="card card--back">
    <svg class="card__waves" viewBox="0 0 616 353" aria-hidden="true">
      <path fill="var(--gold)" d="M0,287 C150,300 300,330 420,303 C505,283 560,262 616,253 L616,353 L0,353 Z"/>
      <path fill="var(--navy)" d="M0,311 C150,320 300,348 430,331 C520,317 580,300 616,292 L616,353 L0,353 Z"/>
    </svg>

    <div class="brand back__brand back__brand--left">
      <div class="brand__circle" style="width:90px;height:90px"></div>
      <div class="brand__name">Borderline Surety Associates</div>
      <div class="back__url">www.borderlinesuretyassociates.example</div>
    </div>

    <div class="brand back__brand back__brand--right">
      <div class="brand__circle" style="width:74px;height:74px;margin-top:16px"></div>
      <div class="brand__name">Cellgate Release Partners</div>
      <div class="back__url">www.cellgatereleasepartners.example</div>
    </div>
  </section>

</main>
</body>
</html>
```